Facebook Header Design Project.

I'm supplying white and colored logos. The Facebook page already exists. URL = https://www.pagebook.example/lumocrest.design The design should not be based on what's already there. Consider mobile implications of the design. This Design will form the designs of other social media headers. LumoCrest is a web design | digital marketing company.

Target Market(s)

People interested in web design | digital marketing services.

Industry/Entity Type

LumoCrest is a web design | digital marketing company. That should be clear in the design.

Colors
0054AA
0677BA
7BADD7
CADEEF
E8F1F8

Requirements
Must have
• Logo. Use Facebook header image dimension.
Nice to have
• Use a color scheme like the logo and feel free to add a color or two from the other side of the color whee.

```html
<!DOCTYPE html>
<html lang="en">
<head>
<meta charset="utf-8">
<title>LumoCrest – Web Design | Digital Marketing Header</title>
<link rel="stylesheet" href="https://fonts.googleapis.com/css2?family=Montserrat:wght@700;800&display=swap">
<style>
  :root {
    --brand-deep: #0054AA;
    --brand-mid: #0677BA;
    --brand-soft: #7BADD7;
    --brand-pale: #CADEEF;
    --brand-mist: #E8F1F8;
    --band-navy: #0b3f95;
    --stripe-navy: #0a3a8c;
    --white: #ffffff;
    --desk-dark: #5a4234;
    --desk-light: #9a7a63;
  }
  * { margin: 0; padding: 0; box-sizing: border-box; }
  html, body { width: 1200px; height: 457px; overflow: hidden; background: var(--white); }
  .header {
    position: relative;
    width: 1200px;
    height: 457px;
    overflow: hidden;
    font-family: "Montserrat", Arial, sans-serif;
    color: var(--white);
    background:
      radial-gradient(circle at 30% 55%, rgba(123,173,215,0.35), transparent 55%),
      linear-gradient(120deg, var(--brand-mid) 0%, #1560b8 45%, var(--brand-deep) 100%);
  }
  .graphics { position: absolute; inset: 0; }
  .tagline-band {
    position: absolute;
    top: 28px;
    left: 0;
    width: 620px;
    height: 44px;
    background: var(--band-navy);
    clip-path: polygon(0 0, 100% 0, 97% 100%, 0 100%);
  }
  .tagline {
    position: absolute;
    top: 34px;
    left: 58px;
    font-size: 27px;
    font-weight: 800;
    letter-spacing: 0.3px;
    line-height: 32px;
    white-space: nowrap;
  }
  .contacts {
    position: absolute;
    top: 81px;
    left: 127px;
    display: flex;
    gap: 26px;
    list-style: none;
  }
  .contact {
    display: flex;
    align-items: center;
    gap: 9px;
    font-size: 10.5px;
    font-weight: 700;
    white-space: nowrap;
  }
  .contact-icon {
    width: 22px;
    height: 22px;
    border-radius: 50%;
    background: var(--white);
    display: flex;
    align-items: center;
    justify-content: center;
  }
  .contact-icon svg { width: 13px; height: 13px; }
  .brand-name {
    position: absolute;
    top: 193px;
    left: 72px;
    font-size: 92px;
    font-weight: 800;
    line-height: 1;
    letter-spacing: -1px;
    white-space: nowrap;
  }
</style>
</head>
<body>
<div class="header">
  <svg class="graphics" width="1200" height="457" viewBox="0 0 1200 457">
    <defs>
      <linearGradient id="deskTone" x1="0" y1="0" x2="1" y2="1">
        <stop offset="0" stop-color="var(--desk-light)"/>
        <stop offset="0.5" stop-color="var(--desk-dark)"/>
        <stop offset="1" stop-color="#b38a6c"/>
      </linearGradient>
    </defs>
    <polygon class="stripe-light" points="694,0 706,0 772,457 760,457" fill="var(--white)"/>
    <polygon class="stripe-navy" points="706,0 742,0 808,457 772,457" fill="var(--stripe-navy)"/>
    <polygon class="photo-area" role="img"
      aria-label="Photo: team working at a desk with laptops, tablet, notebooks and marketing charts"
      points="742,0 1200,0 1200,457 808,457" fill="url(#deskTone)"/>
    <polygon class="stripe-navy-edge" points="1150,0 1200,0 1200,457 1168,457 1175,160" fill="var(--stripe-navy)"/>
    <polygon class="stripe-light-edge" points="1140,0 1150,0 1175,160 1168,457 1160,457 1166,165" fill="var(--white)"/>
  </svg>

  <div class="tagline-band"></div>
  <h2 class="tagline">WEB DESIGN | DIGITAL MARKETING</h2>

  <ul class="contacts">
    <li class="contact">
      <span class="contact-icon">
        <svg viewBox="0 0 24 24"><path fill="var(--band-navy)" d="M6.6 10.8a15.1 15.1 0 0 0 6.6 6.6l2.2-2.2c.3-.3.7-.4 1-.2 1.1.4 2.3.6 3.6.6.6 0 1 .4 1 1V20c0 .6-.4 1-1 1A17 17 0 0 1 3 4c0-.6.4-1 1-1h3.5c.6 0 1 .4 1 1 0 1.3.2 2.5.6 3.6.1.3 0 .7-.2 1z"/></svg>
      </span>
      YOUR PHONE
    </li>
    <li class="contact">
      <span class="contact-icon">
        <svg viewBox="0 0 24 24"><g fill="none" stroke="var(--band-navy)" stroke-width="2.2"><circle cx="12" cy="12" r="9"/><ellipse cx="12" cy="12" rx="4" ry="9"/><line x1="3" y1="12" x2="21" y2="12"/></g></svg>
      </span>
      YOUR WEB ADDRESS
    </li>
    <li class="contact">
      <span class="contact-icon">
        <svg viewBox="0 0 24 24"><rect x="3" y="6" width="18" height="12" rx="1.5" fill="var(--band-navy)"/><path d="M3.5 6.8 12 13l8.5-6.2" fill="none" stroke="var(--white)" stroke-width="1.6"/></svg>
      </span>
      YOUR EMAIL ADDRESS
    </li>
  </ul>

  <h1 class="brand-name">LumoCrest</h1>
</div>
</body>
</html>
```